Postcard Design

We are a pet resort located near Atlanta's Pembrook Calloway Airport. I want a postcard that will show dogs playing and the offer will be "New customers receive 50% off boarding" *
* 50% offer applies to standard lodging fees only. Amenities and playtimes not included in this offer. Valid for up to 10 nights of boarding. Blackout dates of July 4th, Thanksgiving week and Christmas week apply. Reservations required.
The backside of the postcard will read, "New daycare customers recieve ONE WEEK of FREE daycare for your dog".*
* offer good for 5 consecutive days of daycare only-not in conjuction with overnight lodging. Good for one pet per family only. Offer not valid on July 4th week, Thanksgiving week or Christmas week.

```html
<!DOCTYPE html>
<html lang="en">
<head>
<meta charset="utf-8">
<title>Runway Romp Pet Resort – Daycare Postcard</title>
<link rel="stylesheet" href="https://fonts.googleapis.com/css2?family=Alfa+Slab+One&family=Rokkitt:wght@400;500&display=swap">
<style>
  :root {
    --paper: #ffffff;
    --teal-bg: #a0d9d9;
    --teal-ink: #3aa9b4;
    --paw-tint: #d6eeee;
    --plum: #5e4c8c;
    --coral: #e8553a;
  }
  html, body {
    margin: 0;
    padding: 0;
    width: 1200px;
    height: 862px;
    overflow: hidden;
    background: var(--paper);
  }
  .postcard {
    position: relative;
    width: 1200px;
    height: 862px;
    background: var(--paper);
    font-family: "Rokkitt", Georgia, serif;
  }
  .card-face {
    position: absolute;
    left: 73px;
    top: 0;
    width: 1119px;
    height: 862px;
    background: var(--teal-bg);
    overflow: hidden;
  }
  .paw-decoration {
    position: absolute;
    left: 0;
    top: 160px;
    width: 650px;
    height: 630px;
    border-radius: 48% 52% 45% 55% / 50% 45% 55% 50%;
    background: radial-gradient(ellipse at 55% 55%, var(--paw-tint) 0%, var(--paw-tint) 55%, rgba(214,238,238,0) 75%);
  }
  .resort-name {
    position: absolute;
    left: 0;
    top: 52px;
    width: 900px;
    margin: 0;
    font-family: "Alfa Slab One", Georgia, serif;
    font-weight: 400;
    font-size: 66px;
    line-height: 66px;
    color: var(--teal-ink);
    letter-spacing: 2px;
  }
  .resort-name .line-one { display: block; padding-left: 50px; }
  .resort-name .line-two { display: block; padding-left: 250px; }
  .contact {
    position: absolute;
    top: 203px;
    left: 104px;
    margin: 0;
    font-size: 29px;
    color: var(--plum);
    white-space: nowrap;
  }
  .contact .email { margin-left: 60px; }
  .divider {
    position: absolute;
    left: 0;
    top: 247px;
    width: 1119px;
    height: 6px;
  }
  .offer {
    position: absolute;
    left: 0;
    top: 280px;
    width: 660px;
    height: 560px;
    text-align: center;
    color: var(--plum);
  }
  .offer-arc {
    position: absolute;
    left: 0;
    top: 0;
    width: 660px;
    height: 80px;
  }
  .offer-arc text {
    font-family: "Rokkitt", Georgia, serif;
    font-size: 38px;
    fill: var(--coral);
  }
  .offer-headline {
    position: absolute;
    left: 0;
    top: 70px;
    width: 660px;
    margin: 0;
    font-family: "Alfa Slab One", Georgia, serif;
    font-weight: 400;
    color: var(--plum);
    letter-spacing: 3px;
  }
  .offer-headline .big { display: block; font-size: 56px; line-height: 60px; }
  .offer-headline .small { display: block; font-size: 24px; line-height: 26px; letter-spacing: 1px; }
  .offer-tagline {
    position: absolute;
    left: 0;
    top: 220px;
    width: 660px;
    margin: 0;
    font-size: 38px;
    color: var(--coral);
  }
  .offer-terms {
    position: absolute;
    left: 0;
    top: 290px;
    width: 660px;
    margin: 0;
    font-size: 23px;
    line-height: 37px;
  }
  .offer-terms .fine { display: block; font-size: 16px; line-height: 30px; }
</style>
</head>
<body>
<main class="postcard">
  <section class="card-face">
    <div class="paw-decoration" role="img" aria-label="Large faint paw print decoration"></div>

    <h1 class="resort-name">
      <span class="line-one">Runway Romp</span>
      <span class="line-two">Pet Resort</span>
    </h1>

    <p class="contact">
      <span class="website">RunwayRompPets.com</span>
      <span class="email">hello@runwayromppets.com</span>
    </p>

    <svg class="divider" viewBox="0 0 1119 6" preserveAspectRatio="none" aria-hidden="true">
      <path d="M0 3 C 300 5, 700 1, 1119 2" stroke="var(--plum)" stroke-width="3" fill="none"/>
    </svg>

    <div class="offer">
      <svg class="offer-arc" viewBox="0 0 660 80" aria-hidden="false">
        <path id="offer-arc-path" d="M42 72 Q 290 -10 540 72" fill="none"/>
        <text><textPath href="#offer-arc-path" startOffset="50%" text-anchor="middle">New daycare customers recieve</textPath></text>
      </svg>
      <h2 class="offer-headline">
        <span class="big">ONE WEEK</span>
        <span class="small">of</span>
        <span class="big">FREE DAYCARE</span>
      </h2>
      <p class="offer-tagline">for your dog!</p>
      <p class="offer-terms">
        Offer good for 5 consecutive days of daycare only-<br>
        not in cunjunction with overnight lodging.<br>
        Good for one pet per family only.
        <span class="fine">Offer not valid on July 4th week, Thanksgiving week or Christmas week.</span>
      </p>
    </div>
  </section>
</main>
</body>
</html>
```